Brand new website for global research and investment startup

We need a simple website, maybe 3 pages: landing page with business description, investment philosophy, team and contact info.
We have a logo already that can be incorporated. Please use the logo only, not the text
We like the color green, something along the lines of #3D6C32 as the main color.
We'd like to design the website with geometric shapes in gradations of the base color. The shapes should suggest "work in progress", "built to last (a long time)", "solidity" and "indestructibility". One idea floating in my head sees smaller features with icosahedron and dodecahedron shapes, and maybe larger structures like crystal lattices; but please feel free to be creative and imagine your own.

```html
<!DOCTYPE html>
<html lang="en">
<head>
<meta charset="UTF-8">
<title>Ardent Vale — Research That Endures</title>
<link href="https://fonts.googleapis.com/css2?family=Roboto:wght@300;400;500;700&display=swap" rel="stylesheet">
<style>
:root{
  --green:#3d6c32;
  --green-bright:#4fae3c;
  --ink:#111;
  --body:#555;
  --hero-bg:#060b08;
  --pale:#e9eee7;
  --white:#fff;
}
*{margin:0;padding:0;box-sizing:border-box}
html,body{width:1200px;height:3905px;overflow:hidden}
body{position:relative;font-family:"Roboto",sans-serif;background:var(--white);color:var(--ink)}
.abs{position:absolute}
.brand{font-family:"Roboto",sans-serif;font-weight:500;color:var(--white);line-height:1;white-space:nowrap}

/* hero */
.hero{left:0;top:0;width:1200px;height:790px;background:radial-gradient(ellipse at 75% 45%,#0f2a14 0%,var(--hero-bg) 60%)}
.hero-art{left:640px;top:120px;width:560px;height:590px;background:radial-gradient(circle at 55% 45%,#6ee25a 0%,#2f8a2a 30%,#0c2a12 62%,rgba(6,11,8,0) 75%)}
.header-brand{left:110px;top:42px;font-size:32px}
.nav{top:48px;font-size:16px;color:var(--white);font-weight:500}
.nav.active{color:var(--green-bright)}
.nav-underline{left:552px;top:76px;width:46px;height:2px;background:var(--green-bright)}
.btn{display:flex;align-items:center;justify-content:center;background:var(--green);color:var(--white);font-weight:700;font-size:15px;border-radius:4px;text-transform:uppercase}
.contact-btn{left:983px;top:36px;width:102px;height:46px}
.hero-title{left:108px;top:212px;font-size:56px;font-weight:700;line-height:74px;color:var(--white)}
.hero-title span{color:var(--green)}
.hero-text{left:112px;top:443px;width:450px;font-size:14px;line-height:25px;color:var(--white)}
.hero-btn{left:113px;top:552px;width:231px;height:46px}
.wave{left:0;top:690px}

/* about */
.hex-img{left:112px;top:905px}
.about-title{left:645px;top:880px;font-size:42px;line-height:55px;font-weight:400;color:var(--ink)}
.about-title b{color:var(--green);font-weight:700}
.about-text{left:645px;top:1015px;width:445px;font-size:13px;line-height:29.5px;color:var(--body);text-align:justify}
.about-btn{left:645px;top:1207px;width:111px;height:46px}

/* foundation */
.foundation{left:0;top:1398px;width:1200px;height:580px;background:var(--pale)}
.section-title{width:1200px;left:0;text-align:center;font-size:44px;font-weight:400}
.section-title b{color:var(--green);font-weight:700}
.pillar{top:1555px;width:250px;text-align:center}
.pillar h3{font-size:21px;font-weight:500;margin-top:22px;color:var(--ink)}
.pillar.on h3{color:var(--green)}
.pillar p{font-size:12.5px;line-height:26px;color:var(--body);margin-top:10px;padding:0 10px}
.divider{top:1558px;height:320px;border-left:1px dashed #c4cbc2}

/* why */
.why-title{left:110px;top:2070px;font-size:44px;font-weight:400}
.why-title b{color:var(--green);font-weight:700}
.why-text{left:110px;top:2148px;width:420px;font-size:14px;line-height:25px;color:#222}
.why-list{left:112px;top:2248px;list-style:none}
.why-list li{display:flex;align-items:center;gap:14px;height:37px;font-size:13.5px;color:var(--body)}
.hex-globe{left:672px;top:2078px}

/* cta */
.cta{left:111px;top:2527px;width:977px;height:335px;border-radius:6px;background:linear-gradient(135deg,#0c1a0e 0%,#23502a 45%,#0e2211 75%,#2d5f2f 100%);text-align:center;color:var(--white)}
.cta h2{margin-top:55px;font-size:42px;font-weight:400}
.cta h2 b{font-weight:700}
.cta p{margin:22px auto 0;width:660px;font-size:14.5px;line-height:25px}
.cta-btn{display:inline-flex;margin-top:25px;background:var(--white);color:var(--green);padding:0 12px;height:45px;align-items:center;font-weight:700;font-size:14.5px;border-radius:4px}

/* process */
.process-title{top:2960px;font-size:44px}
.process-text{left:230px;top:3030px;width:740px;text-align:center;font-size:15px;line-height:28px;color:var(--body)}
.step{font-size:17px;color:#444;white-space:nowrap}
.step-icon{width:64px;height:64px;border:2.5px solid var(--green);border-radius:50%;background:var(--white);display:flex;align-items:center;justify-content:center}
.process-brand{left:480px;top:3235px;width:226px;text-align:center;font-size:34px;color:var(--green)}

/* footer */
.footer{left:0;top:3490px;width:1200px;height:415px;background:linear-gradient(160deg,#2f5a27 0%,#3d6c32 45%,#2b5424 100%)}
.foot-wave{left:0;top:3478px}
.foot-h{font-size:19px;font-weight:700;color:var(--white);letter-spacing:.5px}
.foot-links{left:113px;top:3665px;list-style:none;color:var(--white);font-size:16px;font-weight:500}
.foot-links li{height:33.5px}
.foot-brand{left:410px;top:3695px;width:370px;text-align:center;font-size:50px}
.social{top:3792px;width:30px;height:30px;border-radius:50%;background:var(--white)}
.contact-item{left:878px;display:flex;align-items:center;gap:14px;color:var(--white);font-size:14px}
.foot-line{left:111px;top:3868px;width:978px;height:1px;background:rgba(255,255,255,.45)}
.copyright{left:0;top:3880px;width:1200px;text-align:center;font-size:14px;color:var(--white)}
</style>
</head>
<body>

<!-- HERO -->
<section class="hero abs"></section>
<div class="hero-art abs" role="img" aria-label="Glowing green polyhedron crystal above a digital grid"></div>
<div class="header-brand brand abs">Ardent Vale</div>
<a class="nav active abs" style="left:552px">Home</a>
<div class="nav-underline abs"></div>
<a class="nav abs" style="left:652px">Investment Philosophy</a>
<a class="nav abs" style="left:880px">Team</a>
<a class="btn contact-btn abs">Contact</a>
<h1 class="hero-title abs">Research That<br>Endures.<span>Investments</span><br>That Last.</h1>
<p class="hero-text abs">We are a Switzerland-based global research and investment firm dedicated to identifying enduring opportunities through disciplined analysis, independent thinking, and a long-term perspective.</p>
<a class="btn hero-btn abs">Explore our philosophy</a>
<svg class="wave abs" width="1200" height="110" viewBox="0 0 1200 110">
  <path d="M0 70 C120 30 200 10 300 40 C420 80 520 100 640 85 C780 60 900 20 1000 20 C1100 20 1160 40 1200 60 L1200 110 L0 110Z" fill="var(--green)"/>
  <path d="M0 100 C120 60 200 40 300 60 C420 90 520 105 640 96 C780 80 900 45 1000 45 C1100 45 1160 70 1200 90 L1200 110 L0 110Z" fill="#fff"/>
</svg>

<!-- ABOUT -->
<svg class="hex-img abs" width="345" height="390" viewBox="0 0 345 390" role="img" aria-label="Hexagon photo collage of a hand using a stylus on a tablet with market charts">
  <defs><linearGradient id="hexA" x1="0" y1="0" x2="1" y2="1"><stop offset="0" stop-color="#1c6fb0"/><stop offset=".5" stop-color="#0d2434"/><stop offset="1" stop-color="#3e6f3c"/></linearGradient></defs>
  <polygon points="172,0 345,98 345,292 172,390 0,292 0,98" fill="url(#hexA)"/>
  <path d="M172 0 V200 M172 200 L0 292 M172 200 L345 292" stroke="#fff" stroke-width="14"/>
</svg>
<h2 class="about-title abs"><b>Built on Research.</b><br>Guided by Discipline.</h2>
<p class="about-text abs">Markets evolve, economies shift, and industries transform. Amid constant change, our approach remains grounded in careful research, thoughtful decision-making, and a commitment to preserving and growing capital over the long term. We combine analytical precision with global market insight to uncover opportunities that can withstand economic cycles and create sustainable value for our investors.</p>
<a class="btn about-btn abs">Read more</a>

<!-- FOUNDATION -->
<section class="foundation abs"></section>
<h2 class="section-title abs" style="top:1448px">The Foundation of <b>Every Decision</b></h2>

<div class="pillar abs" style="left:85px">
  <svg width="120" height="130" viewBox="0 0 120 130"><polygon points="60,4 112,34 112,96 60,126 8,96 8,34" fill="none" stroke="#d3d6d2" stroke-width="6"/><polygon points="60,22 98,92 22,92" fill="none" stroke="#d3d6d2" stroke-width="5"/><circle cx="56" cy="61" r="10" fill="#fff" stroke="#333" stroke-width="2.5"/><path d="M63 68 L73 78" stroke="#333" stroke-width="3"/></svg>
  <h3>Independent Research</h3>
  <p>Every investment begins with comprehensive, unbiased research. We develop our own insights rather than relying solely on market consensus.</p>
</div>
<div class="divider abs" style="left:338px"></div>
<div class="pillar abs" style="left:350px">
  <svg width="120" height="130" viewBox="0 0 120 130"><polygon points="60,4 112,34 112,96 60,126 8,96 8,34" fill="none" stroke="#d3d6d2" stroke-width="6"/><polygon points="60,22 98,92 22,92" fill="none" stroke="#d3d6d2" stroke-width="5"/><circle cx="58" cy="62" r="13" fill="#fff" stroke="#333" stroke-width="2.2"/><path d="M58 54 V62 H65" stroke="#333" stroke-width="2.2" fill="none"/><circle cx="70" cy="73" r="6" fill="#fff" stroke="#333" stroke-width="2"/></svg>
  <h3>Long-Term Perspective</h3>
  <p>We focus on durable businesses, structural trends, and opportunities designed to create lasting value over years—not weeks or months.</p>
</div>
<div class="divider abs" style="left:611px"></div>
<div class="pillar on abs" style="left:605px">
  <svg width="120" height="130" viewBox="0 0 120 130"><polygon points="60,4 112,34 112,96 60,126 8,96 8,34" fill="none" stroke="var(--green)" stroke-width="6"/><polygon points="60,22 98,92 22,92" fill="none" stroke="var(--green)" stroke-width="5"/><circle cx="60" cy="66" r="11" fill="var(--green)"/><circle cx="60" cy="50" r="5" fill="var(--green)"/><circle cx="46" cy="58" r="4" fill="var(--green)"/><circle cx="74" cy="58" r="4" fill="var(--green)"/></svg>
  <h3>Global Outlook</h3>
  <p>Our research spans international markets, allowing us to identify opportunities wherever innovation, quality, and long-term growth emerge.</p>
</div>
<div class="divider abs" style="left:862px"></div>
<div class="pillar abs" style="left:870px">
  <svg width="120" height="130" viewBox="0 0 120 130"><polygon points="60,4 112,34 112,96 60,126 8,96 8,34" fill="none" stroke="#d3d6d2" stroke-width="6"/><polygon points="60,22 98,92 22,92" fill="none" stroke="#d3d6d2" stroke-width="5"/><polygon points="60,48 74,74 46,74" fill="#fff" stroke="#333" stroke-width="2.2"/><path d="M60 56 V66 M60 69 V71" stroke="#333" stroke-width="2.2"/></svg>
  <h3>Risk Management</h3>
  <p>Protecting capital is fundamental. Every opportunity is evaluated with careful attention to risk, resilience, and long-term sustainability.</p>
</div>

<!-- WHY -->
<h2 class="why-title abs">Why <b>Choose Us</b></h2>
<p class="why-text abs">We believe lasting investment success comes from combining intellectual curiosity with disciplined execution.<br>Our approach emphasizes:</p>
<ul class="why-list abs">
  <li><svg width="20" height="16" viewBox="0 0 20 16"><path d="M2 8 L8 14 L18 2" stroke="var(--green)" stroke-width="3" fill="none"/></svg>Evidence-based decision making</li>
  <li><svg width="20" height="16" viewBox="0 0 20 16"><path d="M2 8 L8 14 L18 2" stroke="var(--green)" stroke-width="3" fill="none"/></svg>Independent market research</li>
  <li><svg width="20" height="16" viewBox="0 0 20 16"><path d="M2 8 L8 14 L18 2" stroke="var(--green)" stroke-width="3" fill="none"/></svg>Thoughtful capital allocation</li>
  <li><svg width="20" height="16" viewBox="0 0 20 16"><path d="M2 8 L8 14 L18 2" stroke="var(--green)" stroke-width="3" fill="none"/></svg>Long-term partnerships</li>
  <li><svg width="20" height="16" viewBox="0 0 20 16"><path d="M2 8 L8 14 L18 2" stroke="var(--green)" stroke-width="3" fill="none"/></svg>Continuous learning and adaptation</li>
</ul>
<svg class="hex-globe abs" width="316" height="360" viewBox="0 0 316 360" role="img" aria-label="Hexagon collage of a glowing digital globe above an open hand">
  <defs><radialGradient id="hexB" cx=".5" cy=".45" r=".6"><stop offset="0" stop-color="#3c78b8"/><stop offset=".55" stop-color="#142844"/><stop offset="1" stop-color="#0a1020"/></radialGradient></defs>
  <polygon points="158,0 316,90 316,270 158,360 0,270 0,90" fill="url(#hexB)"/>
  <path d="M158 0 V185 M158 185 L0 270 M158 185 L316 270" stroke="#fff" stroke-width="13"/>
</svg>

<!-- CTA -->
<section class="cta abs">
  <h2>Let's <b>Start a Conversation</b></h2>
  <p>Whether you're seeking a long-term investment partner, exploring research-driven strategies, or simply learning more about our approach, we'd be pleased to hear from you.</p>
  <a class="cta-btn">SCHEDULE A CONVERSATION</a>
</section>

<!-- PROCESS -->
<h2 class="section-title process-title abs">A Methodical Process <b>Built for the Future</b></h2>
<p class="process-text abs">Our philosophy is rooted in the belief that successful investing is not about predicting short-term market movements but understanding long-term fundamentals. Our investment process combines:</p>
<div class="process-brand brand abs">Ardent Vale</div>

<div class="step abs" style="left:150px;top:3202px;width:236px;text-align:right">Global economic research</div>
<div class="step-icon abs" style="left:404px;top:3177px"><svg width="34" height="34" viewBox="0 0 34 34"><circle cx="14" cy="14" r="9" fill="none" stroke="#333" stroke-width="2.5"/><path d="M21 21 L30 30" stroke="#333" stroke-width="3"/></svg></div>
<div class="step-icon abs" style="left:724px;top:3181px"><svg width="34" height="34" viewBox="0 0 34 34"><circle cx="17" cy="17" r="12" fill="none" stroke="#333" stroke-width="2.2"/><circle cx="17" cy="17" r="6" fill="none" stroke="#333" stroke-width="2"/></svg></div>
<div class="step abs" style="left:800px;top:3200px">Long-term valuation</div>

<div class="step abs" style="left:110px;top:3312px;width:290px;text-align:right">Company and industry analysis</div>
<div class="step-icon abs" style="left:418px;top:3290px"><svg width="34" height="34" viewBox="0 0 34 34"><circle cx="15" cy="15" r="10" fill="none" stroke="#333" stroke-width="2.5"/><path d="M10 15 L14 19 L20 11" stroke="var(--green)" stroke-width="2.5" fill="none"/><path d="M22 22 L30 30" stroke="#333" stroke-width="3"/></svg></div>
<div class="step-icon abs" style="left:675px;top:3290px"><svg width="36" height="34" viewBox="0 0 36 34"><rect x="4" y="5" width="28" height="18" fill="none" stroke="#333" stroke-width="2.2"/><path d="M9 18 L15 13 L20 16 L27 9" stroke="var(--green)" stroke-width="2.2" fill="none"/><path d="M18 23 V29 M11 29 H25" stroke="#333" stroke-width="2.2"/></svg></div>
<div class="step abs" style="left:756px;top:3312px">Continuous portfolio monitoring</div>

<div class="step-icon abs" style="left:556px;top:3352px"><svg width="32" height="34" viewBox="0 0 32 34"><path d="M6 3 H20 L26 9 V31 H6Z" fill="none" stroke="#333" stroke-width="2.2"/><path d="M10 14 H20 M10 19 H20 M10 24 H16" stroke="#333" stroke-width="2"/><circle cx="21" cy="24" r="5" fill="#fff" stroke="var(--green)" stroke-width="2"/></svg></div>
<div class="step abs" style="left:480px;top:3418px;width:226px;text-align:center">Risk assessment</div>

<!-- FOOTER -->
<footer class="footer abs"></footer>
<svg class="foot-wave abs" width="1200" height="60" viewBox="0 0 1200 60">
  <path d="M0 35 C100 10 180 10 260 30 C360 55 440 45 520 25 C620 0 700 5 780 30 C880 55 980 45 1080 20 C1140 5 1180 5 1200 10 L1200 60 L0 60Z" fill="var(--green)"/>
</svg>
<h4 class="foot-h abs" style="left:112px;top:3622px">QUICK LINKS</h4>
<ul class="foot-links abs">
  <li>Home</li><li>Investment Philosophy</li><li>Team</li><li>Contact Us</li>
</ul>
<div class="foot-brand brand abs">Ardent Vale</div>
<div class="social abs" style="left:532px"></div>
<div class="social abs" style="left:567px"></div>
<div class="social abs" style="left:603px"></div>
<div class="social abs" style="left:638px"></div>
<h4 class="foot-h abs" style="left:878px;top:3628px">CONTACT INFO</h4>
<div class="contact-item abs" style="top:3678px"><svg width="24" height="24" viewBox="0 0 24 24"><path d="M12 2 C7 2 4 6 4 10 C4 16 12 22 12 22 C12 22 20 16 20 10 C20 6 17 2 12 2Z" fill="#fff"/><circle cx="12" cy="10" r="3" fill="var(--green)"/></svg>12 Alder Row, USA 40210</div>
<div class="contact-item abs" style="top:3722px"><svg width="24" height="24" viewBox="0 0 24 24"><circle cx="12" cy="12" r="11" fill="#fff"/><path d="M8 6 L10 6 L11 9 L9.5 10.5 C10.5 12.5 11.5 13.5 13.5 14.5 L15 13 L18 14 L18 16 C18 17 17 18 16 18 C10 17.5 6.5 14 6 8 C6 7 7 6 8 6Z" fill="var(--green)"/></svg>+1 555 010 0199</div>
<div class="contact-item abs" style="top:3762px"><svg width="24" height="24" viewBox="0 0 24 24"><circle cx="12" cy="12" r="11" fill="#fff"/><rect x="6" y="8" width="12" height="9" fill="none" stroke="var(--green)" stroke-width="1.8"/><path d="M6 8 L12 13 L18 8" stroke="var(--green)" stroke-width="1.8" fill="none"/></svg>info@ardentvale.com</div>
<div class="foot-line abs"></div>
<p class="copyright abs">© 2026 &nbsp; Ardent Vale. All rights reserved.</p>

</body>
</html>
```